Modern CNC Machining Facility in Need of Web Site Improvement

Brixton Fabrication and Tooling, LLC is in need of a web site update. We need to highlight both product sales and our manufacturing services offered. We have recently started offering online product sales and need a better ecommerce platform for our customers. We would like the design winner to be able to freelance the project to a fully functioning webpage.
www.brixtonfabrication.example
What we like about our current web site:
Black and red highlight colors
Gear and caliper logo
RNVR Veteran owned business
What we don't like about our current web site:
Unorganized
Doesn't stand out
Looks like it was made in 1995
Online Product sales are awkward

```html
<!DOCTYPE html>
<html lang="en">
<head>
<meta charset="utf-8">
<title>Brixton Fabrication &amp; Tooling, LLC</title>
<link href="https://fonts.googleapis.com/css2?family=Oswald:wght@400;500&family=Open+Sans:ital,wght@0,400;0,600;1,400&display=swap" rel="stylesheet">
<style>
:root{
  --red:#a4171c;
  --red-bright:#c8161d;
  --ink:#222;
  --text:#444;
  --muted:#666;
  --line:#ddd;
  --panel:#f4f4f4;
  --dark:#3d3d3d;
  --btn-dark:#2b2b2b;
}
*{box-sizing:border-box;margin:0;padding:0}
html,body{width:961px;height:1200px;overflow:hidden;background:#fff}
body{font-family:"Open Sans",sans-serif;color:var(--text);position:relative}
.abs{position:absolute}

.top-links{top:10px;right:104px;font-size:10px;color:var(--muted)}
.top-links span{margin:0 5px;color:#999}
.logo-mark{left:104px;top:23px;width:92px;height:92px;border-radius:50%;background:var(--red);border:9px solid var(--ink)}
.brand{left:215px;top:24px;font-family:"Oswald",sans-serif;color:var(--red);font-size:32px;line-height:33px;font-weight:400}
.tagline{left:215px;top:93px;font-size:11px;color:var(--ink)}
.cart{left:774px;top:38px;text-align:left;font-size:11.5px;color:var(--ink)}
.cart b{font-family:"Oswald",sans-serif;font-weight:400;color:var(--red);font-size:14px;display:block}
.cart i{font-style:normal;color:var(--red)}
.cart-icon{left:749px;top:41px}
.search{left:680px;top:82px;width:177px;height:24px;border:1px solid #ccc;background:#f1f1f1;font-size:10px;font-style:italic;color:#888;padding:5px 9px}
.search-btn{left:832px;top:82px;width:25px;height:24px;background:var(--ink)}

.nav{left:104px;top:122px;width:753px;height:41px;background:var(--red);display:flex;justify-content:space-between;align-items:center;padding:0 13px;border-radius:2px}
.nav a{color:#fff;text-decoration:none;font-size:11px;font-weight:600;letter-spacing:.2px}

.hero{left:105px;top:175px;width:751px;height:273px;background:#ddd8d2;border:1px solid #e2e2e2;overflow:hidden}
.hero-art{position:absolute;right:0;top:0;width:380px;height:273px;background:radial-gradient(circle at 55% 55%,#6a5a4a 0,#a89a8c 25%,#d7d0c8 60%,#e2ddd7 100%)}
.hero h1{position:absolute;left:27px;top:72px;font-family:"Oswald",sans-serif;font-weight:400;color:var(--red);font-size:36px}
.hero p{position:absolute;left:29px;top:120px;width:310px;font-size:13px;line-height:18px;color:var(--ink);font-weight:600}
.btn-red{background:var(--red);color:#fff;font-size:12.5px;font-weight:600;letter-spacing:.5px;display:flex;align-items:center;justify-content:center}
.hero .btn-red{position:absolute;left:29px;top:171px;width:101px;height:34px}
.dots{position:absolute;left:29px;top:235px;display:flex;gap:5px}
.dots i{width:10px;height:10px;background:#fff;border-radius:2px}
.dots i:first-child{background:var(--ink)}

.products{left:104px;top:470px;width:753px;height:366px;background:var(--panel);border:1px solid #e8e8e8}
.sec-title{font-family:"Oswald",sans-serif;color:var(--red);font-weight:400;font-size:20px}
.products .sec-title{position:absolute;left:23px;top:13px}
.products .intro{position:absolute;left:24px;top:44px;width:700px;font-size:10.5px;line-height:18.5px;color:var(--ink)}
.card{top:95px;width:155px;height:250px;background:#fff;border:1px solid #d8d8d8;text-align:center}
.card .thumb{width:103px;height:97px;margin:7px auto 0;background:radial-gradient(circle,#7a6350,#c9c2bb 75%)}
.card h3{font-family:"Oswald",sans-serif;font-weight:400;color:var(--red);font-size:14px;margin-top:11px}
.card p{font-size:9.5px;line-height:14.5px;color:var(--text);margin:3px 18px 0}
.card .price{font-size:12px;font-weight:600;color:var(--red);margin-top:9px;letter-spacing:.3px}
.card .add{width:82px;height:22px;background:var(--btn-dark);color:#fff;font-size:9px;font-weight:600;margin:13px auto 0;display:flex;align-items:center;justify-content:center;border-radius:2px}

.box{top:850px;width:240px;height:221px;background:#fff;border:1px solid #e3e3e3}
.box .sec-title{position:absolute;left:15px;top:11px}
.box .photo{position:absolute;left:15px;top:49px;width:209px;height:117px;border:1px solid #ccc}
.box .cap{position:absolute;left:13px;top:177px;font-family:"Oswald",sans-serif;color:var(--ink);font-size:14px;line-height:16px;width:112px}
.box .btn-red{position:absolute;right:14px;top:182px;width:82px;height:23px;font-size:8.5px;background:var(--red-bright);border-radius:2px}
.post{position:absolute;left:16px;width:208px;border-bottom:1px solid #ddd;padding-bottom:5px}
.post:last-child{border-bottom:none}
.post h4{font-family:"Oswald",sans-serif;font-weight:400;color:var(--red);font-size:14px}
.post p{font-size:9.5px;line-height:16px;color:var(--text);margin-top:2px;width:200px}

.footer{left:0;top:1087px;width:961px;height:113px;background:var(--dark);color:#ddd}
.f-logo{position:absolute;left:106px;top:21px;width:36px;height:36px;border-radius:50%;background:var(--red);border:3px solid #222}
.copy{position:absolute;left:105px;top:66px;font-size:9.5px;line-height:16px;color:#ccc}
.copy b{font-weight:400;color:#fff}
.f-head{position:absolute;top:18px;font-family:"Oswald",sans-serif;color:#fff;font-size:14px;font-weight:400}
.email{position:absolute;left:360px;top:46px;width:149px;height:25px;background:#fff;font-size:9.5px;color:#777;padding:6px 8px}
.go{position:absolute;left:514px;top:46px;width:30px;height:25px;background:var(--red);color:#fff;font-family:"Oswald",sans-serif;font-size:12px;display:flex;align-items:center;justify-content:center}
.social{position:absolute;left:597px;top:48px;display:flex;gap:5px}
.social i{width:21px;height:21px;border-radius:50%;background:#fff}
.pay{position:absolute;left:753px;top:50px;display:flex;gap:4px}
.pay span{width:30px;height:17px;background:#fff;font-size:7.5px;font-weight:600;color:var(--ink);display:flex;align-items:center;justify-content:center}
</style>
</head>
<body>

<div class="abs top-links">My Account<span>|</span>Login<span>|</span>Register<span>|</span>Wishlist<span>|</span>Shipping<span>|</span>FAQ</div>
<div class="abs logo-mark" role="img" aria-label="Brixton Fabrication emblem"></div>
<div class="abs brand">Brixton Fabrication &amp;<br>Tooling, LLC</div>
<div class="abs tagline">CNC Milling and Turning Production Machining, Ice Fishing Spears</div>
<svg class="abs cart-icon" width="17" height="14" viewBox="0 0 17 14"><path d="M1 5h15l-2 8H3z" fill="#444"/><path d="M4 5l4-4 4 4" stroke="#444" fill="none" stroke-width="1.5"/></svg>
<div class="abs cart"><b>My Cart</b>$0.00 (<i>0</i> items)</div>
<div class="abs search">Search Keyword..</div>
<div class="abs search-btn"><svg width="25" height="24" viewBox="0 0 25 24"><circle cx="11" cy="10" r="4" stroke="#fff" stroke-width="2" fill="none"/><path d="M14 13l5 5" stroke="#fff" stroke-width="2.5"/></svg></div>

<nav class="abs nav">
  <a>HOME</a><a>ONLINE PRODUCT SALES</a><a>ICE FISHING SPEARS</a><a>ABOUT US</a><a>EQUIPMENT</a><a>BLOG</a><a>CONTACT US</a>
</nav>

<section class="abs hero">
  <div class="hero-art" role="img" aria-label="Steel clock with outstretched wings and a round dial"></div>
  <h1>Gear Clock with Wings</h1>
  <p>CNC plasma cut clock with a rust patina. Clear coat finish. Material is 16ga steel.</p>
  <div class="btn-red">SHOP NOW</div>
  <div class="dots"><i></i><i></i><i></i><i></i></div>
</section>

<section class="abs products">
  <h2 class="sec-title">Our Products</h2>
  <p class="intro">Our company is based on the belief that our customers' needs are of the utmost importance. Our entire team at Brixton Fabrication is committed to meeting those needs. As a result, a high percentage of our business is from repeat customers and referrals.</p>
  <div class="abs card" style="left:24px"><div class="thumb" role="img" aria-label="Polished sun-ray metal clock"></div><h3>Gear Clock with Wings</h3><p>CNC plasma cut clock with a rust patina. Clear coat finish.</p><div class="price">Price: $155.00</div><div class="add">ADD TO CART</div></div>
  <div class="abs card" style="left:207px"><div class="thumb" role="img" aria-label="Winged clock with round dial"></div><h3>Gear Clock with Wings</h3><p>CNC plasma cut clock with a rust patina. Clear coat finish.</p><div class="price">Price: $155.00</div><div class="add">ADD TO CART</div></div>
  <div class="abs card" style="left:391px"><div class="thumb" role="img" aria-label="Rusted gear clock with wings"></div><h3>Gear Clock with Wings</h3><p>CNC plasma cut clock with a rust patina. Clear coat finish.</p><div class="price">Price: $155.00</div><div class="add">ADD TO CART</div></div>
  <div class="abs card" style="left:574px"><div class="thumb" role="img" aria-label="Rusted layered gear clock"></div><h3>Gear Clock with Wings</h3><p>CNC plasma cut clock with a rust patina. Clear coat finish.</p><div class="price">Price: $155.00</div><div class="add">ADD TO CART</div></div>
</section>

<section class="abs box" style="left:104px">
  <h2 class="sec-title">Ice Fishing Spear</h2>
  <div class="photo" role="img" aria-label="Seven-tine ice fishing spear on a wooden surface" style="background:linear-gradient(#d9b98f,#c9a474)"></div>
  <div class="cap">Replaceable Tine Ice Fishing Spear</div>
  <div class="btn-red">VIEW DETAILS</div>
</section>
<section class="abs box" style="left:360px">
  <h2 class="sec-title">Equipment</h2>
  <div class="photo" role="img" aria-label="Green CNC milling machine in a workshop" style="background:linear-gradient(90deg,#8a9a4e,#b9c57a 50%,#6f7d55)"></div>
  <div class="cap">Kestrel KV-JR, CNC Mill</div>
  <div class="btn-red">VIEW DETAILS</div>
</section>
<section class="abs box" style="left:617px">
  <h2 class="sec-title">Blog Posts</h2>
  <div class="post" style="top:46px"><h4>Aliquam ullamcorper tempor ...</h4><p>Vestibulum ante ipsum primis in faucibus orci luctus et ultrices posuere cubilia..</p></div>
  <div class="post" style="top:104px"><h4>Aliquam ullamcorper tempor ...</h4><p>Vestibulum ante ipsum primis in faucibus orci luctus et ultrices posuere cubilia..</p></div>
  <div class="post" style="top:163px"><h4>Aliquam ullamcorper tempor ...</h4><p>Vestibulum ante ipsum primis in faucibus orci luctus et ultrices posuere cubilia..</p></div>
</section>

<footer class="abs footer">
  <div class="f-logo" role="img" aria-label="Brixton Fabrication emblem"></div>
  <div class="copy">Copyright © 2014. <b>BRIXTONFABRICATION.</b><br>All Right Reserved</div>
  <h3 class="f-head" style="left:360px">Subscribe Newsletter</h3>
  <div class="email">Enter Email</div>
  <div class="go">GO</div>
  <h3 class="f-head" style="left:596px">Connect Us</h3>
  <div class="social" aria-label="Social links"><i></i><i></i><i></i><i></i><i></i></div>
  <h3 class="f-head" style="left:752px">Payment Mode</h3>
  <div class="pay"><span>Paxa</span><span>Cardo</span><span>Remito</span></div>
</footer>

</body>
</html>
```